Law Firm Logo and Stationary

I need a logo for my law firm.  The logo should only contain the firm name "Harlow & Harlow, P.C." but we are open to slight additions like underlining or a box.  We are looking for a modern style but not edgy because our target market is businesses and corporations.

I would like a logo that invokes the traditional values of a law firm (trust, integrity, knowledge) but I want an updated look.

To be clear, the logo should only contain the firm name, I am just looking for a font treatment.

The logo color is up to you.  The only initial opinion I have is that bright colors may not fit with the professional look of a law firm. 

I also want to incorporate the new logo into letterhead and business card designs.  The letterhead should include all of the information that is in my current letterhead, which is attached.  The letterhead should be black or grey on white.  The colored logo will go on the website and promotional materials.

For the business card, I would like to have the logo on the top left, the employee name (Colin J. Harlow) on the middle left and the firm information (address, tel, fax, website, email) on right side.  I am open to suggestions if you have better ideas.
Updates

Here are some comments on the initial 8 designs:

a) I am just interested in a font treatment of our firm name, "Harlow & Harlow, P.C."  I do not want any graphics like a gavel or shield. 

b) The full name of the firm must be in the logo.  So I cannot use designs that only have "H & H"

c) EXAMPLES: Here are two websites with examples of law firm logos that just have the firm name.  These are just samples to give you a general idea of what I am looking for.  Check out:  www.qx-legalco.com and www.tarrowmeade-law.com 

In short, I am looking for a simple, clean design that will look modern enough for our website but is also conservative enough to be on letterhead that gets sent to judges and other lawyers.

Also, the sample letterhead is now loaded in the brief so you can see the information I need included in the new letterhead.

Thanks.

Target Market(s)

businesses and corporations.

Industry/Entity Type

Law Firm

Logo Text

Harlow & Harlow, P.C.

Requirements
Must have
• Firm name, "Harlow & Harlow, P.C."

```html
<!DOCTYPE html>
<html lang="en">
<head>
<meta charset="utf-8">
<title>Harlow &amp; Harlow, P.C. — Stationery</title>
<link rel="stylesheet" href="https://fonts.googleapis.com/css2?family=Tinos:wght@400;700&family=Comfortaa:wght@600&display=swap">
<style>
  :root {
    --brand: #c8084f;
    --ink: #111111;
    --paper: #ffffff;
    --backdrop: #eff0f1;
    --serif: "Tinos", "Times New Roman", serif;
    --rounded: "Comfortaa", sans-serif;
  }
  * { margin: 0; padding: 0; box-sizing: border-box; }
  html, body { width: 1200px; height: 1200px; overflow: hidden; }
  body {
    background: radial-gradient(circle at 50% 45%, #f6f6f7 0%, var(--backdrop) 70%, #e6e7e9 100%);
    font-family: var(--serif);
    color: var(--ink);
    position: relative;
  }
  .sheet { position: absolute; background: var(--paper); box-shadow: 0 1px 3px rgba(0,0,0,.08); }

  /* Letterhead */
  .letterhead { left: 66px; top: 150px; width: 652px; height: 844px; }
  .brand-block { position: absolute; background: var(--brand); }
  .letterhead .brand-block { left: 152px; top: 0; width: 116px; height: 116px; }
  .wordmark {
    position: absolute; font-family: var(--serif); font-weight: 700;
    color: var(--ink); white-space: nowrap; letter-spacing: -0.3px; line-height: 1;
  }
  .letterhead .wordmark { left: 75px; top: 124px; font-size: 22px; }
  .masthead { position: absolute; text-align: right; font-size: 9px; line-height: 13px; text-transform: uppercase; color: var(--ink); }
  .letterhead .masthead { right: 75px; top: 16px; }
  .masthead .title { font-weight: 700; font-size: 11px; line-height: 14px; margin-bottom: 3px; }
  .masthead .admitted { margin-top: 20px; }
  .masthead .bars { text-transform: none; }
  .masthead sup { font-size: 6px; line-height: 0; vertical-align: 3px; }
  .contact { position: absolute; font-size: 9px; line-height: 13px; color: var(--ink); }
  .letterhead .contact { left: 75px; top: 760px; }

  /* Business card front */
  .card-front { left: 755px; top: 337px; width: 354px; height: 215px; }
  .card-front .brand-block { left: 75px; top: 0; width: 83px; height: 83px; }
  .card-front .wordmark { left: 19px; top: 90px; font-size: 16px; }
  .card-front .masthead { right: 20px; top: 12px; }
  .card-front .masthead .admitted { margin-top: 17px; }
  .card-front .contact { left: 20px; top: 121px; font-size: 11px; line-height: 16.7px; }

  /* Business card back */
  .card-back { left: 755px; top: 576px; width: 354px; height: 216px; background: var(--brand); }
  .card-back .window { position: absolute; left: 75px; top: 0; width: 82px; height: 54px; background: var(--paper); }
  .tagline {
    position: absolute; left: 22px; top: 64px; z-index: 1; font-family: var(--rounded); font-weight: 600;
    color: var(--paper); font-size: 17px; line-height: 1; white-space: nowrap; letter-spacing: -0.2px;
  }
</style>
</head>
<body>
  <section class="sheet letterhead" aria-label="Letterhead">
    <div class="brand-block"></div>
    <div class="wordmark">Harlow &amp; Harlow P.C.</div>
    <div class="masthead">
      <div class="title">Law Offices</div>
      <div>Martin E. Harlow<sup>†#</sup></div>
      <div>Colin J. Harlow<sup>†*</sup></div>
      <div>Walter Harlow (1916-1994)</div>
      <div class="admitted">Admitted to Practice</div>
      <div class="bars"><sup>†</sup>District of Columbia &nbsp;▪&nbsp; <sup>#</sup>Maryland &nbsp;▪&nbsp; <sup>*</sup>New York</div>
    </div>
    <div class="contact">
      <div>2210 Alder Street</div>
      <div>Fairbrook&nbsp; MD&nbsp; 20915</div>
      <div>T: 555.01 0 3822&nbsp; F: 555.01 0 8406</div>
      <div>www.harlowpc.com</div>
      <div>Writer’s email: martin.harlow@harlowpc.com</div>
    </div>
  </section>

  <section class="sheet card-front" aria-label="Business card front">
    <div class="brand-block"></div>
    <div class="wordmark">Harlow &amp; Harlow P.C.</div>
    <div class="masthead">
      <div class="title">Law Offices</div>
      <div>Martin E. Harlow<sup>†#</sup></div>
      <div class="admitted">Admitted to Practice</div>
      <div class="bars"><sup>†</sup>District of Columbia &nbsp;▪&nbsp; <sup>#</sup>Maryland</div>
    </div>
    <div class="contact">
      <div>2210 Alder Street</div>
      <div>Fairbrook&nbsp; MD&nbsp; 20915</div>
      <div>T: 555.01 0 3822&nbsp; F: 555.01 0 8406</div>
      <div>www.harlowpc.com</div>
      <div>Writer’s email: martin.harlow@harlowpc.com</div>
    </div>
  </section>

  <section class="sheet card-back" aria-label="Business card back">
    <div class="window"></div>
    <div class="tagline">thinkinside &nbsp;outside the box</div>
  </section>
</body>
</html>
```